Design eBook Cover for Homeowner Association (HOA) book

We need a cover design for an eBook entitled "The Residents Council Leader's Manual: Practical Steps and Proven Methods".

Title: The Residents Council Leader's Manual

Subtitle: Practical Steps and Proven Methods

Name of Author: Gerald Whitcombe, CMA

Style: Professional Guide

Testimonial: "This book is an indispensable tool for anyone on an HOA board. The expert advice and practical approach in 'The Residents Council Leader's Manual' have made a world of difference in our community. Every board member should have a copy!"
— Marla Quint, HOA Board President

I have uploaded a file as design inspiration but not locked into the colors or look. Just want a clean, professional looking cover.

Target Market(s)

Board members of HOAs (Homeowners associations) in the United States

Industry/Entity Type

Real Estate, HOA

Requirements
Must have
• Clean, professional appearance that conveys authority

```html
<!DOCTYPE html>
<html lang="en">
<head>
<meta charset="utf-8">
<title>The Residents Council Leader's Manual — eBook Cover</title>
<link href="https://fonts.googleapis.com/css2?family=Lato:wght@400;700;900&family=Poppins:wght@700&display=swap" rel="stylesheet">
<style>
  :root {
    --page: #ffffff;
    --cover-teal: #50b5c6;
    --navy: #1b3a52;
    --white: #ffffff;
  }
  * { margin: 0; padding: 0; box-sizing: border-box; }
  html, body {
    width: 1200px;
    height: 1200px;
    overflow: hidden;
    background: var(--page);
  }
  .canvas {
    position: relative;
    width: 1200px;
    height: 1200px;
  }
  .cover {
    position: absolute;
    left: 290px;
    top: 104px;
    width: 620px;
    height: 991px;
    background: var(--cover-teal);
    text-align: center;
  }
  .subtitle {
    position: absolute;
    top: 38px;
    left: 0;
    width: 100%;
    font-family: "Lato", sans-serif;
    font-weight: 700;
    font-size: 23px;
    line-height: 34px;
    letter-spacing: 0.3em;
    text-transform: uppercase;
    color: var(--navy);
    padding-left: 0.3em;
  }
  .house-art {
    position: absolute;
    left: 28px;
    top: 157px;
    width: 553px;
    height: 186px;
  }
  .title {
    position: absolute;
    top: 386px;
    left: 0;
    width: 100%;
    font-family: "Poppins", sans-serif;
    font-weight: 700;
    font-size: 66px;
    line-height: 62px;
    text-transform: uppercase;
    color: var(--white);
  }
  .title span { display: block; }
  .testimonial {
    position: absolute;
    top: 746px;
    left: 40px;
    width: 540px;
    font-family: "Lato", sans-serif;
    color: var(--navy);
  }
  .testimonial-quote {
    font-size: 16.5px;
    line-height: 23px;
    font-weight: 400;
  }
  .testimonial-rule {
    width: 30px;
    height: 2px;
    background: var(--navy);
    margin: 7px auto 10px;
  }
  .testimonial-source {
    font-size: 17px;
    font-weight: 700;
    letter-spacing: -0.01em;
  }
  .author {
    position: absolute;
    top: 918px;
    left: 0;
    width: 100%;
    font-family: "Lato", sans-serif;
    font-weight: 900;
    font-size: 34px;
    letter-spacing: 0.12em;
    text-transform: uppercase;
    color: var(--white);
    padding-left: 0.12em;
  }
</style>
</head>
<body>
  <main class="canvas">
    <section class="cover">
      <p class="subtitle">Practical Steps<br>and Proven Methods</p>

      <svg class="house-art" viewBox="0 0 553 186" role="img" aria-label="Illustration of house rooflines with a small four-pane window">
        <defs>
          <linearGradient id="roofTone" x1="0" y1="0" x2="1" y2="1">
            <stop offset="0" stop-color="#1b3a52" stop-opacity="0.28"/>
            <stop offset="1" stop-color="#1b3a52" stop-opacity="0.12"/>
          </linearGradient>
        </defs>
        <rect x="0" y="0" width="553" height="186" fill="url(#roofTone)"/>
      </svg>

      <h1 class="title">
        <span>The</span>
        <span>Residents</span>
        <span>Council</span>
        <span>Leader's</span>
        <span>Manual</span>
      </h1>

      <blockquote class="testimonial">
        <p class="testimonial-quote">"This book is an indispensable tool for anyone on an HOA board. The expert advice and practical approach in 'The Residents Council Leader's Manual' have made a world of difference in our community. Every board member should have a copy!"</p>
        <div class="testimonial-rule"></div>
        <p class="testimonial-source">Marla Quint, HOA Board President</p>
      </blockquote>

      <p class="author">Gerald Whitcombe, CMA</p>
    </section>
  </main>
</body>
</html>
```